Business cards for 3 Realtors at one brokerage

We will need a business card template that can be projected on 3 business cards. Harborline Homes & Capital Corp. has 3 realtors on staff Dale, Owen, and Marcus. We all want a business card that shows our new logo and information. I will attach many versions of our Logo as well as head shots for each realtor (Owen- Long hair, youngest. Marcus- Suit jacket, parted hair cut. Dale- Angled Pose, Shirt and Tie.) I have attached our information below.

Dale Pinsworth
801-555-0147
dale@harborlinehomesco.com
Principal Broker

Marcus Ferndale
801-555-0192
marcus@harborlinehomesco.com
Real Estate Agent

Owen Ferndale
801-555-0163
owen@harborlinehomesco.com
Real Estate Agent

Harborline Homes & Capital Corp.
HarborlineHomesCo.com
2918 E 8250 Suite 207-316, Maple Bend, UT 84990

Please feel free to reach out with any questions, comments, or concerns.

```html
<!DOCTYPE html>
<html lang="en">
<head>
<meta charset="utf-8">
<title>Harborline Homes &amp; Capital Corp. — Business Card</title>
<link rel="stylesheet" href="https://fonts.googleapis.com/css2?family=Montserrat:wght@600&family=Arimo:wght@400&display=swap">
<style>
  :root {
    --backdrop: #202020;
    --card-white: #ffffff;
    --slate: #707070;
    --slate-text: #5e5e5e;
    --sky: #38aaf0;
    --ink: #1f1f1f;
    --light: #ffffff;
  }
  * { box-sizing: border-box; margin: 0; padding: 0; }
  html, body {
    width: 1075px; height: 1200px; overflow: hidden;
    background: var(--backdrop);
  }
  .card {
    position: absolute; left: 206px; width: 663px;
    box-shadow: 2px 3px 4px rgba(0,0,0,.6);
    overflow: hidden;
  }
  .card--front { top: 187px; height: 396px; background: var(--card-white); }
  .card--back { top: 637px; height: 395px; background: var(--slate); }

  .brand-mark {
    position: absolute; border-radius: 50%;
    border: 4px solid var(--sky);
  }
  .brand-name {
    position: absolute; text-align: center;
    font-family: "Montserrat", sans-serif; font-weight: 600;
    line-height: 1;
  }
  .card--front .brand-mark { left: 120px; top: 31px; width: 100px; height: 100px; }
  .card--front .brand-name { left: 10px; width: 318px; top: 142px; color: var(--slate-text); }
  .brand-name__main { display: block; font-size: 26px; letter-spacing: .5px; }
  .brand-name__sub { display: block; font-size: 12px; letter-spacing: 3px; margin-top: 8px; }

  .agent { position: absolute; left: 33px; top: 219px; }
  .agent__name {
    font-family: "Montserrat", sans-serif; font-weight: 600;
    font-size: 23px; color: var(--sky); line-height: 1;
  }
  .agent__title {
    font-family: "Arimo", sans-serif; font-size: 18px; color: var(--ink);
    line-height: 1.2; margin-top: 2px;
  }
  .agent__rule {
    position: absolute; left: 36px; top: 276px; width: 221px; height: 5px;
    background: var(--sky);
  }
  .headshot {
    position: absolute; left: 374px; top: 16px; width: 252px; height: 263px;
    background: radial-gradient(ellipse at 50% 35%, #c98d72 0%, #8a5a3c 45%, #eef1f5 80%, #ffffff 100%);
    border-radius: 45% 45% 0 0;
  }

  .contact-band {
    position: absolute; left: 0; top: 279px; width: 100%; height: 117px;
    background: var(--slate); color: var(--light);
    font-family: "Arimo", sans-serif; font-size: 17px;
  }
  .contact-list { position: absolute; left: 35px; top: 20px; list-style: none; }
  .contact-list li { display: flex; align-items: center; height: 24px; }
  .contact-list svg { width: 17px; height: 17px; margin-right: 7px; flex: none; }
  .office-address {
    position: absolute; right: 40px; top: 44px; text-align: right;
    font-style: normal; line-height: 24px;
  }

  .card--back .brand-mark { left: 261px; top: 84px; width: 141px; height: 141px; }
  .card--back .brand-name { left: 0; width: 100%; top: 246px; color: var(--light); }
  .card--back .brand-name__main { font-size: 38px; letter-spacing: 1px; }
  .card--back .brand-name__sub { font-size: 16px; letter-spacing: 4px; margin-top: 13px; }
  .web-band {
    position: absolute; left: 0; bottom: 0; width: 100%; height: 45px;
    background: var(--sky); color: var(--light);
    font-family: "Arimo", sans-serif; font-size: 18px;
    display: flex; align-items: center; justify-content: center;
  }
</style>
</head>
<body>
  <section class="card card--front">
    <div class="brand-mark" aria-hidden="true"></div>
    <div class="brand-name">
      <span class="brand-name__main">HARBORLINE HOMES</span>
      <span class="brand-name__sub">&amp; CAPITAL CORP.</span>
    </div>
    <div class="agent">
      <h1 class="agent__name">OWEN FERNDALE</h1>
      <p class="agent__title">Real Estate Agent</p>
    </div>
    <div class="agent__rule"></div>
    <div class="headshot" role="img" aria-label="Headshot of Owen Ferndale"></div>

    <div class="contact-band">
      <ul class="contact-list">
        <li>
          <svg viewBox="0 0 24 24" aria-hidden="true"><path fill="#38aaf0" d="M6.6 10.8a15.1 15.1 0 0 0 6.6 6.6l2.2-2.2a1 1 0 0 1 1-.25 11.4 11.4 0 0 0 3.6.57 1 1 0 0 1 1 1V20a1 1 0 0 1-1 1A17 17 0 0 1 3 4a1 1 0 0 1 1-1h3.5a1 1 0 0 1 1 1c0 1.250.2 2.450.57 3.570a1 1 0 0 1-.25 1z"/></svg>
          801-555-0163
        </li>
        <li>
          <svg viewBox="0 0 24 24" aria-hidden="true"><rect x="2" y="5" width="20" height="14" fill="#38aaf0"/><path d="M2 5l10 8 10-8" fill="none" stroke="#707070" stroke-width="1.6"/></svg>
          owen@harborlinehomesco.com
        </li>
        <li>
          <svg viewBox="0 0 24 24" aria-hidden="true"><g fill="none" stroke="#38aaf0" stroke-width="2"><circle cx="12" cy="12" r="9"/><ellipse cx="12" cy="12" rx="4" ry="9"/><path d="M3 12h18M5 7h14M5 17h14"/></g></svg>
          www.HarborlineHomesCo.com
        </li>
      </ul>
      <address class="office-address">
        2918 E 8250 Suite 207-316<br>
        Maple Bend, UT 84990
      </address>
    </div>
  </section>

  <section class="card card--back">
    <div class="brand-mark" aria-hidden="true"></div>
    <div class="brand-name">
      <span class="brand-name__main">HARBORLINE HOMES</span>
      <span class="brand-name__sub">&amp; CAPITAL CORP.</span>
    </div>
    <div class="web-band">www.HarborlineHomesCo.com</div>
  </section>
</body>
</html>
```